Dale Morrikan Plumbing and Heating

Need a card design for a plumbing and heating company that does service and repair, remodels, and plumbing in new construction. Please add following on back side of card; Boilers, Water heaters, Gas lines, Sump pumps, Toilet repairs, Faucet repairs, Pipe thawing, Radiant heating, New construction, Remodels.

Industry/Entity Type

Plumber

Contact Information for Business Card

Was thinking white gloss card with colored logo in middle or black glossy card with silver logo in middle. Just a thought but very open to other designs.

Requirements
Must have
• Need following on front of card;
• P(203) 321-8689
• C(203) 232-9069
• Dale Morrikan 275 Larkwell St West, Stamford, Ct 06214
• service@DrainHearth.example (plumbing in blue, heating in red)
• www.DrainHearth.example (plumbing in blue, heating in red)
• Fully Licensed and Insured
Nice to have
• Elegant design

```html
<!DOCTYPE html>
<html lang="en">
<head>
<meta charset="utf-8">
<title>Dale Morrikan Plumbing and Heating – Business Card</title>
<link rel="stylesheet" href="https://fonts.googleapis.com/css2?family=Open+Sans:wght@400;600;700&display=swap">
<style>
  :root {
    --brand-blue: #2e3aa6;
    --brand-blue-deep: #222c86;
    --brand-blue-light: #4a58c8;
    --brand-red: #a81f2f;
    --ink: #1e1e24;
    --muted: #55565e;
    --card-white: #fbfbfb;
    --backdrop: #e9e7e3;
    --rule: #c9c9cf;
  }
  * { box-sizing: border-box; margin: 0; padding: 0; }
  html, body {
    width: 1200px; height: 1023px; overflow: hidden;
    background: var(--backdrop);
    font-family: "Open Sans", Arial, sans-serif;
  }
  .stage { position: relative; width: 1200px; height: 1023px; }

  .card {
    position: absolute;
    width: 760px; height: 434px;
    border-radius: 10px;
    overflow: hidden;
    box-shadow: 0 10px 26px rgba(0,0,0,.18);
  }

  /* ---------- Front ---------- */
  .card-front { left: 60px; top: 50px; background: linear-gradient(135deg, #ffffff 0%, var(--card-white) 60%, #ececef 100%); }
  .front-brand {
    position: absolute; left: 40px; top: 150px; width: 330px;
    display: flex; align-items: center; gap: 14px;
  }
  .brand-dot { flex: none; width: 34px; height: 34px; border-radius: 50%; background: var(--brand-blue); }
  .brand-name {
    font-weight: 700; font-size: 22px; line-height: 1.2;
    color: var(--brand-blue); text-transform: uppercase; letter-spacing: .5px;
  }
  .front-divider {
    position: absolute; left: 395px; top: 50px; width: 1px; height: 300px;
    background: linear-gradient(to bottom, transparent, var(--rule) 20%, var(--rule) 80%, transparent);
  }
  .contact { position: absolute; left: 425px; top: 52px; width: 320px; color: var(--ink); }
  .person-name { font-size: 30px; font-weight: 700; color: var(--brand-blue); line-height: 1.1; }
  .person-title { font-size: 19px; color: var(--muted); margin: 4px 0 14px; }
  .contact-line { display: flex; align-items: center; gap: 10px; font-size: 17px; line-height: 1.55; }
  .contact-line svg { flex: none; width: 16px; height: 16px; }
  .blue { color: var(--brand-blue); }
  .red { color: var(--brand-red); }
  .address { margin-top: 6px; font-size: 17px; line-height: 1.45; }
  .address .company { color: var(--brand-blue); }
  .front-band { position: absolute; left: 0; bottom: 0; width: 100%; height: 42px; display: flex; }
  .band-blue { flex: 0 0 455px; background: var(--brand-blue); }
  .band-red {
    flex: 1; background: var(--brand-red); color: #fff;
    font-size: 16px; display: flex; align-items: center; padding-left: 20px;
  }

  /* ---------- Back ---------- */
  .card-back {
    left: 380px; top: 540px;
    background: radial-gradient(ellipse at 40% 35%, var(--brand-blue-light) 0%, var(--brand-blue) 45%, var(--brand-blue-deep) 100%);
  }
  .back-brand {
    position: absolute; left: 0; right: 0; top: 120px;
    display: flex; justify-content: center; align-items: center; gap: 14px;
  }
  .back-brand .brand-dot { background: #d7d9e2; }
  .back-brand .brand-name { color: #d7d9e2; font-size: 24px; }
  .services-band {
    position: absolute; left: 0; bottom: 0; width: 100%; height: 118px;
    background: #ffffff; padding: 16px 30px 0;
  }
  .services-heading { font-size: 19px; font-weight: 700; font-style: italic; color: var(--brand-red); }
  .services-list { font-size: 16.5px; color: var(--brand-blue); line-height: 1.5; margin-top: 4px; }
</style>
</head>
<body>
<div class="stage">

  <section class="card card-front" aria-label="Business card front">
    <div class="front-brand">
      <span class="brand-dot"></span>
      <span class="brand-name">Dale Morrikan Plumbing and Heating</span>
    </div>
    <div class="front-divider"></div>
    <div class="contact">
      <p class="person-name">Evan Brandt</p>
      <p class="person-title">President</p>
      <p class="contact-line">
        <svg viewBox="0 0 16 16"><rect x="4" y="1" width="8" height="14" rx="1.5" fill="none" stroke="#1e1e24" stroke-width="1.5"/></svg>
        (203) 555-0183
      </p>
      <p class="contact-line">
        <svg viewBox="0 0 16 16"><path d="M2 6c0-2 2-3 6-3s6 1 6 3v1h-3V5.5H5V7H2z" fill="#1e1e24"/><rect x="3" y="8" width="10" height="6" rx="1" fill="#1e1e24"/></svg>
        (203) 555-0147
      </p>
      <p class="contact-line">
        <svg viewBox="0 0 16 16"><rect x="1" y="3" width="14" height="10" rx="1" fill="#1e1e24"/><path d="M1.5 3.5 8 9l6.5-5.5" fill="none" stroke="#fff" stroke-width="1.2"/></svg>
        <span>service@<span class="blue">Drain</span><span class="red">Hearth</span>.example</span>
      </p>
      <p class="contact-line">
        <svg viewBox="0 0 16 16"><circle cx="8" cy="8" r="7" fill="#1e1e24"/><path d="M1 8h14M8 1c-3 3.5-3 10.5 0 14M8 1c3 3.5 3 10.5 0 14" fill="none" stroke="#fff" stroke-width="1"/></svg>
        <span>www.<span class="blue">Drain</span><span class="red">Hearth</span>.example</span>
      </p>
      <p class="address">
        <span class="company">Dale Morrikan</span><br>
        275 Larkwell St West<br>
        Stamford, Ct 06214
      </p>
    </div>
    <div class="front-band">
      <div class="band-blue"></div>
      <div class="band-red">Fully Licensed and Insured</div>
    </div>
  </section>

  <section class="card card-back" aria-label="Business card back">
    <div class="back-brand">
      <span class="brand-dot"></span>
      <span class="brand-name">Dale Morrikan Plumbing and Heating</span>
    </div>
    <div class="services-band">
      <p class="services-heading">We Specialize In:</p>
      <p class="services-list">
        Boilers, Water heaters, Gas lines, Sump pumps, Toilet repairs<br>
        Faucet repairs, Pipe thawing, Radiant heating, New construction, Remodels
      </p>
    </div>
  </section>

</div>
</body>
</html>
```